ORB of Quietharbour Business Card Rebrand

Hello Designers! We are looking for help designing our new business card to go in conjunction with our company rebrand. Unfortunately, we have an event mid June that requires we get these printed ASAP (before our new website is launched.) We have a mostly complete Brand Book which I have uploaded to this request for your reference to company information, style, fonts. I've also enclosed our logo file in .eps & .jpg. Attached is a sample business card my boss liked but said was "too simple." I made it in Canva and do not profess to be a designer. NOT FOR DESIGN REFERENCE, ONLY FOR CONTEXT Here is what our old website looks like: https://orbofquietharbour.example/.
Sick
Gathering more feedback
Sick
Sick

```html
<!DOCTYPE html>
<html lang="en">
<head>
<meta charset="utf-8">
<title>ORB of Quietharbour – Business Card</title>
<link rel="stylesheet" href="https://fonts.googleapis.com/css2?family=Poppins:wght@400;500;700&display=swap">
<style>
  :root {
    --bg: #c3c4c6;
    --paper: #ffffff;
    --brand-blue: #4ab1e6;
    --brand-blue-deep: #1f9bd6;
    --tint: #dbeef9;
    --ink: #1c1c1c;
    --ink-soft: #3a3a3a;
  }
  * { box-sizing: border-box; margin: 0; padding: 0; }
  html, body { width: 1200px; height: 876px; overflow: hidden; }
  body {
    background: var(--bg);
    font-family: "Poppins", sans-serif;
    display: flex;
    align-items: center;
    justify-content: center;
    gap: 48px;
  }
  .card {
    position: relative;
    width: 525px;
    height: 300px;
    border-radius: 4px;
    overflow: hidden;
    box-shadow: 0 10px 24px rgba(0,0,0,0.18);
  }

  /* Front */
  .card--front { background: var(--paper); }
  .front__motif {
    position: absolute;
    right: -70px;
    bottom: -120px;
    width: 340px;
    height: 340px;
    border-radius: 50%;
    background: var(--tint);
  }
  .brand {
    display: flex;
    align-items: center;
    gap: 10px;
  }
  .brand__dot {
    width: 30px;
    height: 30px;
    border-radius: 50%;
    background: var(--brand-blue);
    flex: none;
  }
  .brand__name {
    font-weight: 700;
    font-size: 22px;
    color: var(--ink);
    letter-spacing: 0.01em;
    line-height: 1;
  }
  .front__brand { position: absolute; left: 150px; top: 30px; }
  .front__details { position: absolute; left: 40px; top: 92px; }
  .person__name {
    font-weight: 700;
    font-size: 22px;
    color: var(--ink);
    line-height: 1.1;
  }
  .person__role {
    font-size: 12px;
    color: var(--brand-blue);
    margin-bottom: 12px;
  }
  .contact { list-style: none; }
  .contact__item {
    display: flex;
    align-items: center;
    gap: 8px;
    font-size: 13px;
    color: var(--ink-soft);
    line-height: 1.75;
  }
  .contact__icon { width: 12px; height: 12px; flex: none; }
  .contact__base {
    font-weight: 500;
    font-size: 13px;
    color: var(--brand-blue);
    margin-top: 6px;
  }

  /* Back */
  .card--back {
    background: linear-gradient(135deg, var(--brand-blue-deep) 0%, var(--brand-blue) 55%, #62bdeb 100%);
  }
  .back__brand {
    position: absolute;
    left: 50%;
    top: 50%;
    transform: translate(-50%, -50%);
  }
  .back__brand .brand__dot { background: var(--paper); width: 40px; height: 40px; }
  .back__brand .brand__name { font-size: 28px; }
</style>
</head>
<body>

  <section class="card card--front" aria-label="Business card front">
    <div class="front__motif" role="img" aria-label="Large faint brand symbol decoration"></div>

    <div class="brand front__brand">
      <span class="brand__dot"></span>
      <span class="brand__name">ORB of Quietharbour</span>
    </div>

    <div class="front__details">
      <h1 class="person__name">Mara Ellison-Vance</h1>
      <p class="person__role">Managing Partner</p>
      <ul class="contact">
        <li class="contact__item">
          <svg class="contact__icon" viewBox="0 0 12 12" aria-hidden="true"><path d="M2.5 1h2l1 2.8-1.3 1a6 6 0 0 0 3 3l1-1.3 2.8 1v2a1 1 0 0 1-1 1A9.5 9.5 0 0 1 1.5 2a1 1 0 0 1 1-1z" fill="#4ab1e6"/></svg>
          +945-555-0142
        </li>
        <li class="contact__item">
          <svg class="contact__icon" viewBox="0 0 12 12" aria-hidden="true"><rect x="0.5" y="2" width="11" height="8" rx="1" fill="#4ab1e6"/><path d="M1 2.6l5 3.8 5-3.8" stroke="#fff" stroke-width="1" fill="none"/></svg>
          mara@orbofquietharbour.example
        </li>
        <li class="contact__item">
          <svg class="contact__icon" viewBox="0 0 12 12" aria-hidden="true"><circle cx="6" cy="6" r="5.5" fill="#4ab1e6"/><path d="M0.8 6h10.4M6 0.6c2 2.6 2 8.2 0 10.8M6 0.6c-2 2.6-2 8.2 0 10.8" stroke="#fff" stroke-width="0.8" fill="none"/></svg>
          orbofquietharbour.example
        </li>
      </ul>
      <p class="contact__base">Harlow Bay, GA based (Central Time)</p>
    </div>
  </section>

  <section class="card card--back" role="img" aria-label="Business card back with repeating brand symbol pattern on blue">
    <div class="brand back__brand">
      <span class="brand__dot"></span>
      <span class="brand__name">ORB of Quietharbour</span>
    </div>
  </section>

</body>
</html>
```